loyalty card design needed

Inner city Coffee shop/cafe- we need a loyalty card that will stand out in wallets.
Ideally we are wanting up to 4 rows of 10 sign boxes.

needs a note on it to say tenth coffee is free.

Target Market(s)

business people

Industry/Entity Type

Cafe

Contact Information for Business Card

LANTERN ROAST
47 Pelling Street
HOBART TASMANIA 7000
phone 03 62915384
www.lanternroast.com.au

Logo Text

LANTERN ROAST

Logo styles of interest
Wordmark Logo
Requirements
Must have
• Ideally we are wanting up to 4 rows of 10 sign boxes.

needs a note on it to say tenth coffee is free

colours as suggested in file upload
Nice to have
• really stand out form the rest of cards in a customers wallet.

```html
<!DOCTYPE html>
<html lang="en">
<head>
<meta charset="utf-8">
<title>Lantern Roast Loyalty Card</title>
<link rel="stylesheet" href="https://fonts.googleapis.com/css2?family=Gelasio:wght@400;700&display=swap">
<style>
  :root {
    --orange-deep: #e06a14;
    --orange-mid: #f09a55;
    --orange-soft: #f8cfae;
    --cream: #fff8f3;
    --ink: #111111;
    --slot-line: #2b2b2b;
    --slot-fill: rgba(255, 255, 255, 0.55);
    --ghost-word: rgba(170, 150, 140, 0.45);
    --ghost-cup: rgba(150, 140, 135, 0.35);
  }
  * { margin: 0; padding: 0; box-sizing: border-box; }
  html, body { width: 1200px; height: 693px; overflow: hidden; background: #ffffff; }
  .loyalty-card {
    position: relative;
    width: 1200px;
    height: 693px;
    overflow: hidden;
    font-family: "Gelasio", Georgia, serif;
    color: var(--ink);
    background:
      radial-gradient(ellipse 330px 260px at 40px 20px, var(--orange-deep) 0%, rgba(240,154,85,0.6) 45%, rgba(255,255,255,0) 100%),
      radial-gradient(ellipse 420px 520px at 1220px 240px, var(--orange-deep) 0%, var(--orange-mid) 45%, rgba(248,207,174,0.4) 75%, rgba(255,255,255,0) 100%),
      radial-gradient(ellipse 360px 300px at 120px 640px, var(--orange-mid) 0%, rgba(248,207,174,0.5) 50%, rgba(255,255,255,0) 100%),
      radial-gradient(ellipse 300px 220px at 1100px 720px, var(--orange-mid) 0%, rgba(255,255,255,0) 100%),
      var(--cream);
  }
  .decor-cup {
    position: absolute;
    left: 830px;
    top: 190px;
    width: 380px;
    height: 500px;
    border-radius: 40% 40% 30% 30%;
    background: radial-gradient(ellipse at 50% 65%, var(--ghost-cup) 0%, rgba(150,140,135,0.15) 55%, rgba(150,140,135,0) 80%);
  }
  .stamp-row { position: absolute; left: 0; width: 1200px; height: 70px; }
  .stamp-row--top { top: 64px; }
  .stamp-row--bottom { top: 561px; }
  .stamp-slot { fill: var(--slot-fill); stroke: var(--slot-line); stroke-width: 2.5; }
  .ghost-word {
    position: absolute;
    font-size: 20px;
    color: var(--ghost-word);
    white-space: nowrap;
  }
  .ghost-word--cappuccino { left: 628px; top: 185px; transform: rotate(14deg); }
  .ghost-word--java { left: 134px; top: 283px; transform: rotate(-24deg); }
  .ghost-word--coffee { left: 1068px; top: 208px; transform: rotate(-16deg); }
  .ghost-word--espresso { left: 266px; top: 490px; transform: rotate(16deg); }
  .ghost-word--latte { left: 1004px; top: 530px; transform: rotate(20deg); }
  .offer {
    position: absolute;
    font-size: 23px;
    line-height: 28px;
    white-space: nowrap;
  }
  .offer--upper { left: 79px; top: 196px; }
  .offer--lower { left: 755px; top: 471px; }
  .business {
    position: absolute;
    left: 0;
    width: 1204px;
    top: 272px;
    text-align: center;
  }
  .business__name { font-size: 31px; font-weight: 700; letter-spacing: 0.5px; margin-bottom: 12px; }
  .business__line { font-size: 20px; font-weight: 700; line-height: 29px; }
</style>
</head>
<body>
<main class="loyalty-card">
  <div class="decor-cup" role="img" aria-label="Large faint steaming coffee cup decoration"></div>

  <svg class="stamp-row stamp-row--top" viewBox="0 0 1200 70" aria-label="Stamp boxes 1 to 10">
    <rect class="stamp-slot" x="68" y="3" width="64" height="64" rx="8"/>
    <rect class="stamp-slot" x="181" y="3" width="64" height="64" rx="8"/>
    <rect class="stamp-slot" x="295" y="3" width="64" height="64" rx="8"/>
    <rect class="stamp-slot" x="408" y="3" width="64" height="64" rx="8"/>
    <rect class="stamp-slot" x="521" y="3" width="64" height="64" rx="8"/>
    <rect class="stamp-slot" x="635" y="3" width="64" height="64" rx="8"/>
    <rect class="stamp-slot" x="748" y="3" width="64" height="64" rx="8"/>
    <rect class="stamp-slot" x="861" y="3" width="64" height="64" rx="8"/>
    <rect class="stamp-slot" x="973" y="3" width="64" height="64" rx="8"/>
    <rect class="stamp-slot" x="1073" y="3" width="64" height="64" rx="8"/>
  </svg>

  <span class="ghost-word ghost-word--cappuccino">Cappuccino</span>
  <span class="ghost-word ghost-word--java">Java</span>
  <span class="ghost-word ghost-word--coffee">Coffee</span>
  <span class="ghost-word ghost-word--espresso">Espresso</span>
  <span class="ghost-word ghost-word--latte">Latte</span>

  <p class="offer offer--upper">Buy 9 cups, Get the 10th Cup FREE!</p>

  <section class="business">
    <h1 class="business__name">LANTERN ROAST</h1>
    <p class="business__line">47 Pelling Street HOBART</p>
    <p class="business__line">TASMANIA 7000</p>
    <p class="business__line">Phone: 03 62915384</p>
    <p class="business__line">www.lanternroast.com.au</p>
  </section>

  <p class="offer offer--lower">Buy 9 cups, Get the 10th Cup FREE!</p>

  <svg class="stamp-row stamp-row--bottom" viewBox="0 0 1200 70" aria-label="Stamp boxes 11 to 20">
    <rect class="stamp-slot" x="68" y="3" width="64" height="64" rx="8"/>
    <rect class="stamp-slot" x="181" y="3" width="64" height="64" rx="8"/>
    <rect class="stamp-slot" x="295" y="3" width="64" height="64" rx="8"/>
    <rect class="stamp-slot" x="408" y="3" width="64" height="64" rx="8"/>
    <rect class="stamp-slot" x="521" y="3" width="64" height="64" rx="8"/>
    <rect class="stamp-slot" x="635" y="3" width="64" height="64" rx="8"/>
    <rect class="stamp-slot" x="748" y="3" width="64" height="64" rx="8"/>
    <rect class="stamp-slot" x="861" y="3" width="64" height="64" rx="8"/>
    <rect class="stamp-slot" x="973" y="3" width="64" height="64" rx="8"/>
    <rect class="stamp-slot" x="1073" y="3" width="64" height="64" rx="8"/>
  </svg>
</main>
</body>
</html>
```